Accounting firm needing business card / letterhead designed
Marcus T. Elbering, CPA
marcus@fernquill.com
www.fernquill.com
482 N Harlow Ave Ashcombe, WV 43719
419-555-0172

```html
<!DOCTYPE html>
<html lang="en">
<head>
<meta charset="utf-8">
<title>Fernquill Solutions — Business Card</title>
<link rel="stylesheet" href="https://fonts.googleapis.com/css2?family=Roboto:wght@300;400;500;700&family=Roboto+Condensed:wght@500&display=swap">
<style>
  :root {
    --navy: #24205c;
    --green: #7dbd3a;
    --paper: #f4f4f2;
    --backdrop: #e6e3de;
    --white: #ffffff;
    --grey-text: #555555;
  }
  * { margin: 0; padding: 0; box-sizing: border-box; }
  html, body { width: 1200px; height: 960px; overflow: hidden; }
  body {
    background: var(--backdrop);
    position: relative;
    font-family: "Roboto", Arial, sans-serif;
  }
  .card {
    position: absolute;
    width: 600px;
    height: 343px;
    background: var(--paper);
    box-shadow: 0 3px 8px rgba(0,0,0,0.25);
    overflow: hidden;
  }
  .card--front { left: 314px; top: 113px; }
  .card--back  { left: 311px; top: 472px; }

  .contact-panel {
    position: absolute;
    left: 309px; top: 0;
    width: 291px; height: 343px;
    background: var(--navy);
  }
  .web-band {
    position: absolute;
    left: 0; top: 284px;
    width: 600px; height: 31px;
    background: var(--green);
    color: var(--white);
    font-size: 15px;
    font-weight: 300;
    letter-spacing: 7.5px;
    line-height: 31px;
    padding-left: 126px;
    text-transform: uppercase;
  }
  .web-band strong { font-weight: 700; }

  .wordmark {
    position: absolute;
    text-align: center;
    color: var(--navy);
    font-weight: 500;
    line-height: 1;
  }
  .wordmark__name { display: block; }
  .wordmark__tag { display: block; }

  .card--front .wordmark { left: 20px; width: 270px; top: 124px; }
  .card--front .wordmark__name { font-size: 42px; letter-spacing: 1px; }
  .card--front .wordmark__tag { font-size: 15px; letter-spacing: 4px; margin-top: 8px; }

  .card--back .wordmark { left: 0; width: 600px; top: 118px; }
  .card--back .wordmark__name { font-size: 58px; letter-spacing: 2px; }
  .card--back .wordmark__tag { font-size: 21px; letter-spacing: 6px; margin-top: 12px; }

  .contact {
    position: absolute;
    left: 368px; top: 95px;
    color: var(--white);
  }
  .contact__name {
    font-family: "Roboto Condensed", "Arial Narrow", sans-serif;
    font-weight: 500;
    font-size: 22px;
    color: var(--green);
    margin-bottom: 15px;
  }
  .contact__address { font-size: 14px; line-height: 18px; margin-bottom: 11px; }
  .contact__line {
    display: flex; align-items: center; gap: 8px;
    font-size: 14px; line-height: 20px;
  }
  .contact__line svg { width: 13px; height: 13px; flex: none; }

  .back-url {
    position: absolute;
    left: 0; width: 600px; top: 282px;
    text-align: center;
    font-size: 14px;
    letter-spacing: 8.5px;
    color: var(--grey-text);
  }
</style>
</head>
<body>
  <section class="card card--front" aria-label="Business card front">
    <div class="wordmark">
      <span class="wordmark__name">FERNQUILL</span>
      <span class="wordmark__tag">SOLUTIONS</span>
    </div>
    <div class="contact-panel"></div>
    <div class="web-band">www.<strong>fernquill</strong>.com</div>
    <div class="contact">
      <p class="contact__name">Marcus T. Elbering, CPA</p>
      <p class="contact__address">482 N Harlow Ave<br>Ashcombe, WV 43719</p>
      <p class="contact__line">
        <svg viewBox="0 0 24 24" aria-hidden="true"><path fill="#7dbd3a" d="M6.6 10.8c1.4 2.8 3.8 5.1 6.6 6.6l2.2-2.2c.3-.3.7-.4 1-.2 1.1.4 2.3.6 3.6.6.6 0 1 .4 1 1V20c0 .6-.4 1-1 1C10.6 21 3 13.4 3 4c0-.6.4-1 1-1h3.5c.6 0 1 .4 1 1 0 1.3.2 2.5.6 3.6.1.3 0 .7-.2 1l-2.3 2.2z"/></svg>
        419-555-0172
      </p>
      <p class="contact__line">
        <svg viewBox="0 0 24 24" aria-hidden="true"><path fill="#7dbd3a" d="M2 5h20v14H2z"/><path fill="none" stroke="#24205c" stroke-width="2" d="M2 5l10 8 10-8"/></svg>
        marcus@fernquill.com
      </p>
    </div>
  </section>

  <section class="card card--back" aria-label="Business card back">
    <div class="wordmark">
      <span class="wordmark__name">FERNQUILL</span>
      <span class="wordmark__tag">SOLUTIONS</span>
    </div>
    <p class="back-url">www.fernquill.com</p>
  </section>
</body>
</html>
```